Redesign of a facility management homepage

We need a redesign/an improved design of the facility management homepage (http://www.kolvenhaus-drefling.de/).
This websites offers detailed information on the "About us" as company, the "Services" provided and special information on facility and strata management. We would like to keep the structure of the website.
We need ideas/designs how this website could look more modern and confidential and appealing/pleasant for visitors at the same time and not losing the main purpose of information distribution.
The green color must be used since this is the basic color from our logo.
The blue in the background of the logo ist optional. So feel to use it or not.
We need no coding only design (.psd or as .ai)
Industry/Entity Type
It Company
Look and feel
Each slider illustrates characteristics of the customer's brand and the style your logo design should communicate.

```html
<!DOCTYPE html>
<html lang="de">
<head>
<meta charset="utf-8">
<title>Kolvenhaus Büro- und Hausmeisterservice</title>
<link href="https://fonts.googleapis.com/css2?family=Arimo:wght@400;500;700&display=swap" rel="stylesheet">
<style>
:root{
  --green-dark:#2d5a36;
  --green-logo:#3d9a42;
  --header-bg:#e7e8e9;
  --tile-bg:#dcdddf;
  --footer-bg:#e2e3e4;
  --text:#333;
  --text-soft:#555;
  --white:#fff;
}
*{margin:0;padding:0;box-sizing:border-box}
html,body{width:1200px;height:990px;overflow:hidden}
body{font-family:"Arimo",Helvetica,Arial,sans-serif;background:var(--white);color:var(--text);position:relative}
.site-header{position:absolute;left:0;top:0;width:1200px;height:181px;background:var(--header-bg)}
.brand{position:absolute;left:182px;top:44px;display:flex;align-items:center;gap:8px}
.brand-mark{width:14px;height:14px;background:var(--green-logo)}
.brand-name{font-size:28px;font-weight:700;color:var(--green-logo);letter-spacing:.5px}
.tagline{position:absolute;left:182px;top:106px;font-size:12px;line-height:16px;color:var(--green-dark)}
.main-nav{position:absolute;right:180px;top:81px;display:flex;gap:37px;font-size:14px;color:var(--green-dark)}
.main-nav a{color:inherit;text-decoration:none;position:relative}
.main-nav a.active{font-weight:700}
.main-nav a.active svg{position:absolute;left:50%;top:24px;margin-left:-6px}
.hero{position:absolute;left:0;top:181px;width:1200px;height:266px}
.hero-photo{position:absolute;inset:0;background:linear-gradient(90deg,#8d8d8d 0%,#a59a7c 25%,#9b8a6a 45%,#c9c2b2 62%,#9a9a98 80%,#a08f6f 100%)}
.hero-caption{position:absolute;left:182px;top:73px;width:418px;height:120px;background:rgba(0,0,0,.62);color:var(--white);padding:20px 22px}
.hero-caption .c1{font-size:23px;letter-spacing:.3px;line-height:26px}
.hero-caption .c2{font-size:15px;font-weight:700;letter-spacing:.6px;margin-top:3px}
.hero-caption .c3{font-size:18px;margin-top:5px;letter-spacing:.3px}
.dots{position:absolute;left:577px;top:232px;display:flex;gap:6px}
.dots span{width:7px;height:7px;border-radius:50%;background:var(--white)}
.dots span.on{background:var(--green-logo)}
.features{position:absolute;left:0;top:494px;width:1200px}
.feature{position:absolute;width:180px;text-align:center}
.feature-icon{width:75px;height:75px;margin:0 auto;background:var(--tile-bg);display:flex;align-items:center;justify-content:center}
.feature h2{margin-top:26px;font-size:16px;font-weight:400;letter-spacing:.6px;color:var(--green-dark);line-height:19px}
.feature p{margin-top:9px;font-size:10.5px;line-height:14.5px;color:var(--text-soft);letter-spacing:.2px}
.company{position:absolute;left:0;top:723px;width:1200px;height:201px;text-align:center}
.company-photo{position:absolute;inset:0;background:linear-gradient(90deg,#dadbdc,#e8e8e8 40%,#dcdcdc 70%,#e6e6e6)}
.company-body{position:relative;padding-top:48px}
.company h3{font-size:16px;font-weight:700;letter-spacing:.8px;color:#111}
.company .address{margin-top:16px;font-size:10px;line-height:18.5px;letter-spacing:.3px;color:#333}
.company .contact{margin-top:15px;font-size:10px;font-weight:700;color:#111}
.company .contact .sep{margin:0 9px}
.site-footer{position:absolute;left:0;top:924px;width:1200px;height:66px;font-size:10px;letter-spacing:.3px;color:#222}
.copyright{position:absolute;left:183px;top:27px}
.footer-nav{position:absolute;right:180px;top:27px;display:flex;gap:29px}
.footer-nav a{color:inherit;text-decoration:none}
</style>
</head>
<body>
<header class="site-header">
  <div class="brand"><span class="brand-mark"></span><span class="brand-name">Kolvenhaus</span></div>
  <p class="tagline">Büro- und Hausmeisterservice<br>GmbH Drefling Ihr Partner vor Ort.</p>
  <nav class="main-nav">
    <a href="#" class="active">Wir über uns<svg width="12" height="8" viewBox="0 0 12 8"><path d="M1 1l5 5 5-5" fill="none" stroke="#2d5a36" stroke-width="2"/></svg></a>
    <a href="#">Gebäudemanagement</a>
    <a href="#">Gebäudeverwaltung</a>
    <a href="#">Vermietung</a>
  </nav>
</header>

<section class="hero">
  <div class="hero-photo" role="img" aria-label="Foto-Collage des Fuhrparks: weiße Lieferwagen und Kleintraktoren mit Schneeschild vor Backsteinhäusern"></div>
  <div class="hero-caption">
    <div class="c1">UNSER FUHRPARK</div>
    <div class="c2">WINTERDIENST UND SCHNEEBERÄUMUNG</div>
    <div class="c3">KOLVENHAUS VOR ORT</div>
  </div>
  <div class="dots"><span class="on"></span><span></span><span></span><span></span></div>
</section>

<section class="features">
  <div class="feature" style="left:194px">
    <div class="feature-icon"><svg width="40" height="40" viewBox="0 0 40 40" fill="none" stroke="#2d5a36" stroke-width="2.5" stroke-linecap="round"><path d="M9 6c-3 2-4 5-2 10 3 8 9 14 17 17 4 1 7 0 9-3l-5-5-4 2c-4-2-7-5-9-9l2-4z" fill="#2d5a36" stroke="none"/><path d="M23 13a5 5 0 0 1 4 4M24 8a10 10 0 0 1 8 8M25 3a15 15 0 0 1 12 12"/></svg></div>
    <h2>SUPPORTSTÖRUNG<br>ONLINE MELDEN</h2>
    <p>Lorem Ipsum is simply dummy text of the printing and typesetting industry.</p>
  </div>
  <div class="feature" style="left:405px">
    <div class="feature-icon"><svg width="38" height="26" viewBox="0 0 38 26"><rect x="0" y="0" width="38" height="26" fill="#2d5a36"/><path d="M1 1l18 14L37 1M1 25l13-12M37 25L24 13" fill="none" stroke="#dcdddf" stroke-width="2"/></svg></div>
    <h2>KONTAKT</h2>
    <p>Lorem Ipsum is simply dummy text of the printing and typesetting industry.</p>
  </div>
  <div class="feature" style="left:616px">
    <div class="feature-icon"><svg width="42" height="42" viewBox="0 0 42 42"><rect x="2" y="6" width="30" height="28" rx="2" fill="none" stroke="#2d5a36" stroke-width="2.5"/><rect x="2" y="6" width="30" height="6" fill="#2d5a36"/><path d="M9 2v7M25 2v7" stroke="#2d5a36" stroke-width="2.5"/><g fill="#2d5a36"><rect x="6" y="15" width="4" height="4"/><rect x="12" y="15" width="4" height="4"/><rect x="18" y="15" width="4" height="4"/><rect x="6" y="21" width="4" height="4"/><rect x="12" y="21" width="4" height="4"/><rect x="6" y="27" width="4" height="4"/></g><circle cx="30" cy="31" r="9" fill="#dcdddf" stroke="#2d5a36" stroke-width="2.5"/><path d="M30 26v5h4" fill="none" stroke="#2d5a36" stroke-width="2.5"/></svg></div>
    <h2>LINKS</h2>
    <p>Lorem Ipsum is simply dummy text of the printing and typesetting industry.</p>
  </div>
  <div class="feature" style="left:826px">
    <div class="feature-icon"><svg width="46" height="44" viewBox="0 0 46 44" fill="none" stroke="#2d5a36" stroke-width="3" stroke-linejoin="round"><path d="M12 17L23 7l11 10v11H12z"/><rect x="20" y="21" width="6" height="7" fill="#2d5a36" stroke="none"/><path d="M3 18c0 10 5 17 16 22M43 18c0 10-5 17-16 22" stroke-linecap="round"/><path d="M8 26c3 4 7 7 11 8M38 26c-3 4-7 7-11 8" stroke-linecap="round"/></svg></div>
    <h2>IMPRESSUM</h2>
    <p>Lorem Ipsum is simply dummy text of the printing and typesetting industry.</p>
  </div>
</section>

<section class="company">
  <div class="company-photo" role="img" aria-label="Blasses Hintergrundfoto weißer Firmenfahrzeuge"></div>
  <div class="company-body">
    <h3>KOLVENHAUS BÜRO- UND HAUSMEISTERSERVICE GMBH</h3>
    <p class="address">LINDENPLATZ 14 IN 04712 DREFLING VERTRETEN DURCH FRAU HELGA RONDORF,<br>GESCHÄFTSFÜHRERIN AG BRÜCKSTADT, HR.NR.: HRB 47215</p>
    <p class="contact">Tel: 0 34 51 / 72 40 13<span class="sep">•</span>Fax: 0 34 51 / 72 40 19<span class="sep">•</span>Mail: info@kolvenhaus-drefling.de and Kontaktformular</p>
  </div>
</section>

<footer class="site-footer">
  <div class="copyright">Kolvenhaus © 2014 | Privacy Policy</div>
  <nav class="footer-nav">
    <a href="#">Wir über uns</a>
    <a href="#">Gebäudemanagement</a>
    <a href="#">Gebäudeverwaltung</a>
    <a href="#">Vermietung</a>
  </nav>
</footer>
</body>
</html>
```